Velkano Holdings Ltd - An invesmtent & trading company needs a web design

We need a web design for our company based in Cyprus. The company was founded in 2009. We have continuously grown and now invest & trade all over the world.

Velkano Holdings ltd. specializes in the buying and selling of crude oil, precious metals and the investment in properties.

We know that trust is of the utmost importance when it comes to business and the design should communicate this to prospective business partners. Find attached the company logo. The colour scheme for the website should use similar colours and ideally incorporate the logo in some shape or form as well.

Target Market(s)

Oil Traders, Metall Traders, Property Investments

Industry/Entity Type

Trade

Coding

Coded - Design and coding required

Number of Pages Required

4 page

Font styles to use
Sans Serif

Requirements
Must have
• Mainpage,
• About Us
• Partners
• Legal Notice

```html
<!DOCTYPE html>
<html lang="en">
<head>
<meta charset="utf-8">
<title>Velkano Holdings Ltd</title>
<link rel="stylesheet" href="https://fonts.googleapis.com/css2?family=Open+Sans:wght@400;600;700;800&family=Montserrat:wght@400;600;700&display=swap">
<style>
:root{
  --navy:#1d3b63;
  --blue:#2f6fb3;
  --sky:#4aa3df;
  --ink:#333a42;
  --muted:#7d848c;
  --line:#e3e6ea;
  --soft:#f4f5f7;
  --dark:#2b2d31;
  --footer:#2e3033;
  --footer-deep:#232528;
  --white:#ffffff;
}
*{margin:0;padding:0;box-sizing:border-box}
html,body{width:1200px;height:2568px;overflow:hidden}
body{font-family:"Open Sans",Arial,sans-serif;color:var(--ink);background:var(--white)}
.header{height:77px;display:flex;align-items:center;justify-content:space-between;padding:0 100px;background:var(--white);border-bottom:1px solid var(--line)}
.brand{display:flex;align-items:center;gap:10px}
.brand-mark{width:30px;height:30px;background:var(--navy)}
.brand-name{font-family:"Montserrat",sans-serif;font-weight:700;font-size:22px;color:var(--navy);letter-spacing:1px}
.nav{display:flex;gap:44px;font-size:12px;font-weight:700;color:var(--ink);text-transform:uppercase}
.hero{position:relative;height:563px;overflow:hidden}
.hero-photo{position:absolute;inset:0;background:linear-gradient(100deg,#dfe7ef 0%,#bccbdc 35%,#8aa2bd 60%,#5f7898 100%)}
.hero-content{position:absolute;left:100px;top:150px;width:380px}
.hero-title{font-family:"Montserrat",sans-serif;font-weight:700;font-size:46px;color:var(--navy);line-height:1}
.hero-title span{font-size:22px;color:var(--navy)}
.hero-text{margin-top:14px;font-size:15px;line-height:1.45;color:var(--navy)}
.btn{display:inline-block;margin-top:26px;padding:14px 26px;background:var(--navy);color:var(--white);font-size:11px;font-weight:700;text-transform:uppercase;border-radius:2px}
.hero-arrow{position:absolute;top:270px;width:26px;height:26px;border-radius:50%;background:rgba(255,255,255,.6);display:flex;align-items:center;justify-content:center}
.hero-arrow.left{left:30px}.hero-arrow.right{right:30px}
.section-title{font-family:"Montserrat",sans-serif;font-size:26px;font-weight:700;text-align:center;color:var(--ink);text-transform:uppercase}
.lead{text-align:center;font-size:13px;font-weight:700;color:var(--ink);margin-top:12px}
.welcome{padding:48px 160px 0;height:253px}
.welcome p.body{margin-top:14px;text-align:center;font-size:12px;line-height:1.8;color:var(--muted)}
.services{height:321px;padding-top:18px;border-top:1px solid var(--line);margin:0 100px}
.cards{display:flex;gap:22px;justify-content:center;margin-top:30px}
.card{width:218px;height:190px;border:1px solid var(--line);background:var(--soft);text-align:center;padding:20px 18px}
.card-icon{width:52px;height:52px;border-radius:50%;margin:0 auto;background:#5a5d62;display:flex;align-items:center;justify-content:center}
.card-icon.active{background:var(--sky)}
.card h3{margin-top:16px;font-size:12px;font-weight:800;text-transform:uppercase;line-height:1.3}
.card p{margin-top:10px;font-size:10px;line-height:1.6;color:var(--muted)}
.about{margin-top:84px;height:390px;position:relative;background:linear-gradient(180deg,#3a3d42,#25272b);color:var(--white);text-align:center;padding-top:58px}
.about h2{font-family:"Montserrat",sans-serif;font-size:76px;font-weight:700;letter-spacing:2px;line-height:1}
.about h2 strong{font-weight:700}
.about h4{margin-top:14px;font-size:20px;font-weight:700;text-transform:uppercase}
.about p{margin:22px auto 0;width:560px;font-size:13px;line-height:1.6;color:#d5d8dc}
.btn-ghost{display:inline-block;margin-top:30px;padding:12px 30px;border:1px solid var(--white);font-size:10px;font-weight:700;text-transform:uppercase}
.clients{height:295px;padding-top:38px}
.testimonial{display:flex;gap:40px;margin:44px auto 0;width:820px;align-items:flex-start}
.avatar{width:120px;height:120px;border-radius:50%;flex:none;background:linear-gradient(135deg,#d0d4d9,#8e959e)}
.quote{font-size:12px;line-height:1.8;color:var(--muted);padding-top:12px}
.quote .who{display:block;margin-top:12px;font-size:11px;font-weight:700;color:var(--sky);text-transform:uppercase}
.quote .role{display:block;font-size:10px;color:var(--muted)}
.partners{height:112px;display:flex;justify-content:space-between;align-items:center;padding:0 120px;border-top:1px solid var(--line)}
.partner{display:flex;align-items:center;gap:8px;font-weight:700;font-size:18px;color:#555}
.partner i{width:14px;height:14px;background:#888;display:block}
.footer{height:440px;background:var(--footer);color:#b4b8bd;padding:42px 100px 0;display:grid;grid-template-columns:1.4fr 1fr 1fr 1fr;gap:40px}
.footer h5{color:var(--white);font-size:12px;font-weight:700;text-transform:uppercase;margin-bottom:18px}
.footer p,.footer li{font-size:11px;line-height:2;list-style:none}
.footer .brand-name{color:#aeb3b9;font-size:20px}
.footer .brand-mark{background:#6d7278;width:24px;height:24px}
.footer .brand{margin-top:26px}
.contact li{display:flex;align-items:center;gap:8px}
.social li{display:flex;align-items:center;gap:10px;margin-bottom:6px}
.social i{width:22px;height:22px;border:1px solid #6a6f75;display:block}
.copyright{height:38px;background:var(--footer-deep);color:#8b9096;font-size:10px;display:flex;align-items:center;justify-content:center}
</style>
</head>
<body>
<header class="header">
  <div class="brand"><span class="brand-mark"></span><span class="brand-name">VELKANO</span></div>
  <nav class="nav"><span>Home</span><span>About Us</span><span>Partners</span><span>Legal Notice</span><span>Contact Us</span></nav>
</header>

<section class="hero">
  <div class="hero-photo" role="img" aria-label="Worker climbing stairs of an oil storage tank under a blue sky"></div>
  <div class="hero-content">
    <h1 class="hero-title">VELKANO <span>HOLDINGS LTD</span></h1>
    <p class="hero-text">specializes in the buying and selling of crude oil, precious metals and the investment in properties.</p>
    <span class="btn">View Our History</span>
  </div>
  <span class="hero-arrow left"><svg width="10" height="10" viewBox="0 0 10 10"><path d="M7 1 3 5l4 4" stroke="#1d3b63" stroke-width="2" fill="none"/></svg></span>
  <span class="hero-arrow right"><svg width="10" height="10" viewBox="0 0 10 10"><path d="M3 1l4 4-4 4" stroke="#1d3b63" stroke-width="2" fill="none"/></svg></span>
</section>

<section class="welcome">
  <h2 class="section-title">Welcome to Velkano Holdings Ltd</h2>
  <p class="lead">Velkano Holdings ltd. specializes in the buying and selling of crude oil, precious metals and the investment in properties.</p>
  <p class="body">Founded in Cyprus in 2009, we have grown steadily and now invest and trade across the world. Trust is at the heart of every partnership we build, and our team works with oil traders, metal traders and property investors who value reliability, transparency and long term commitment in every transaction we make together.</p>
</section>

<section class="services">
  <h2 class="section-title">Services</h2>
  <p class="lead">Velkano Holdings ltd. specializes in the buying and selling of crude oil, precious metals and the investment in properties.</p>
  <div class="cards">
    <div class="card"><div class="card-icon active"><svg width="24" height="24" viewBox="0 0 24 24"><rect x="3" y="12" width="4" height="9" fill="#fff"/><rect x="10" y="7" width="4" height="14" fill="#fff"/><rect x="17" y="3" width="4" height="18" fill="#fff"/></svg></div><h3>Es simplemente el texto de relleno de las</h3><p>Crude oil trading with trusted partners around the world.</p></div>
    <div class="card"><div class="card-icon"><svg width="24" height="24" viewBox="0 0 24 24"><path d="M2 9l10-5 10 5-10 5z" fill="#fff"/><path d="M6 12v5l6 3 6-3v-5" stroke="#fff" stroke-width="2" fill="none"/></svg></div><h3>Es simplemente el texto de relleno de las</h3><p>Precious metals bought and sold with care and insight.</p></div>
    <div class="card"><div class="card-icon"><svg width="24" height="24" viewBox="0 0 24 24"><path d="M4 12l8-7 8 7v8H4z" fill="#fff"/></svg></div><h3>Es simplemente el texto de relleno de las</h3><p>Property investment in stable and growing markets.</p></div>
    <div class="card"><div class="card-icon"><svg width="24" height="24" viewBox="0 0 24 24"><rect x="6" y="2" width="12" height="20" rx="2" fill="#fff"/></svg></div><h3>Es simplemente el texto de relleno de las</h3><p>Personal advice for every partner, wherever you are.</p></div>
  </div>
</section>

<section class="about">
  <h2>ABOUT <strong>VELKANO</strong></h2>
  <h4>Es simplemente el texto de relleno de las imprentas y archivos de texto</h4>
  <p>For over a decade our company has built lasting trade relations across continents, guided by trust, careful research and a clear view of global markets in energy, metals and real estate.</p>
  <span class="btn-ghost">Click here for more info</span>
</section>

<section class="clients">
  <h2 class="section-title">What our client's say</h2>
  <div class="testimonial">
    <div class="avatar" role="img" aria-label="Client portrait"></div>
    <p class="quote">Working with this team has been a pleasure from the very first contact. They are reliable, responsive and always clear about every step of a deal. We have traded with them for years and look forward to many more.<span class="who">Daniel Ostrow</span><span class="role">Managing Director</span></p>
  </div>
</section>

<section class="partners">
  <span class="partner">Norvik</span>
  <span class="partner"><i></i>Strata</span>
  <span class="partner"><i></i>Alvera</span>
  <span class="partner">Corbin</span>
  <span class="partner"><i></i>Tessly</span>
</section>

<footer class="footer">
  <div>
    <h5>Who we are</h5>
    <p>Velkano Holdings ltd. is an investment and trading company based in Cyprus, founded in 2009, active in crude oil, precious metals and property.</p>
    <div class="brand"><span class="brand-mark"></span><span class="brand-name">VELKANO</span></div>
  </div>
  <div>
    <h5>Welcome</h5>
    <ul><li>Home</li><li>About Us</li><li>Partners</li><li>Legal Notice</li><li>Contact Us</li></ul>
  </div>
  <div class="contact">
    <h5>Contact Info</h5>
    <ul>
      <li><svg width="10" height="12" viewBox="0 0 10 12"><path d="M5 0a4 4 0 0 0-4 4c0 3 4 8 4 8s4-5 4-8a4 4 0 0 0-4-4z" fill="#b4b8bd"/></svg>14 Harbour Street, Larnaca</li>
      <li>Cyprus 6020</li>
      <li><svg width="10" height="12" viewBox="0 0 10 12"><path d="M2 0h3l1 3-2 1c1 2 2 3 3 4l1-2 2 1v3c-5 0-8-5-8-10z" fill="#b4b8bd"/></svg>+357 24 000 118</li>
      <li><svg width="12" height="10" viewBox="0 0 12 10"><rect x="0" y="0" width="12" height="10" fill="#b4b8bd"/><path d="M0 0l6 5 6-5" stroke="#2e3033" fill="none"/></svg>info@velkano.example</li>
    </ul>
  </div>
  <div class="social">
    <h5>Follow us</h5>
    <ul><li><i></i>Network one</li><li><i></i>Network two</li><li><i></i>Network three</li><li><i></i>Network four</li></ul>
  </div>
</footer>
<div class="copyright">© Copyright 2016 Velkano Holdings Ltd. All rights reserved.</div>
</body>
</html>
```